Dr. Marisa Tellen Medical/Chiropractic Business Card

Dr. Tellen is a chiropractor and will require a business card that she uses every single day to book appointments on the back side of the card. Currently the office name goes by Dr. Marisa Tellen. The chiropractic profession is based on the diagnosis and manipulative treatment of misalignments of the joints, especially those of the spinal column, which are held to cause other disorders by affecting the nerves, muscles, and organs. Dr. Marisa Tellen is looking for a contemporary and minimalistic design.

Industry/Entity Type

Medical

Contact Information for Business Card

Name: Dr. Marisa Tellen; Address: 748 Ashcombe Rd North, London, ON N5R 2K9; Phone Number: 519.672.4193; Fax: 519.681.2054; email: marisa.tellen@brevanmail.com

Requirements
Must have
• ability to write multiple appointments date/time on the back of card

```html
<!DOCTYPE html>
<html lang="en">
<head>
<meta charset="utf-8">
<title>Dr. Marisa Tellen – Business Card</title>
<link href="https://fonts.googleapis.com/css2?family=Tenor+Sans&display=swap" rel="stylesheet">
<style>
  :root {
    --ink: #000000;
    --paper: #ffffff;
    --stage: #efefef;
    --rule: #222222;
  }
  * { margin: 0; padding: 0; box-sizing: border-box; }
  html, body { width: 1200px; height: 1200px; overflow: hidden; background: var(--stage); }
  body { position: relative; font-family: "Tenor Sans", "Gill Sans", sans-serif; }

  .card {
    position: absolute;
    top: 199px;
    width: 430px;
    height: 750px;
    transform: scale(1.07);
    transform-origin: top left;
    box-shadow: 0 4px 14px rgba(0,0,0,0.18);
    overflow: hidden;
  }
  .card--front { left: 100px; background: var(--ink); color: var(--paper); }
  .card--back { left: 640px; background: var(--paper); color: var(--ink); }

  .stripe { position: absolute; top: 0; bottom: 0; }
  .card--front .stripe { left: 25px; width: 40px; background: var(--paper); }
  .card--back .stripe { left: 25px; width: 40px; background: var(--ink); }

  .doctor-name {
    position: absolute; left: 70px; top: 56px;
    font-size: 31px; font-weight: 400; letter-spacing: 0.3px;
  }

  .contact-list { position: absolute; left: 0; top: 206px; width: 430px; list-style: none; }
  .contact-item { position: absolute; left: 0; display: flex; align-items: flex-start; font-size: 22px; line-height: 24px; }
  .contact-item .icon { position: absolute; left: 29px; top: 0; width: 32px; height: 24px; }
  .contact-item .label { position: absolute; left: 73px; white-space: nowrap; }
  .item-role { top: 4px; }
  .item-phone { top: 40px; }
  .item-fax { top: 76px; }
  .item-email { top: 109px; }
  .item-address { top: 150px; }

  .appointments-title {
    position: absolute; left: 70px; top: 56px;
    font-size: 34px; font-weight: 400;
  }
  .appointments-note {
    position: absolute; left: 73px; top: 98px;
    font-size: 16.5px; line-height: 22px;
  }
  .col-head { position: absolute; top: 208px; font-size: 22px; }
  .col-date { left: 73px; }
  .col-time { left: 305px; }

  .slots { position: absolute; left: 76px; top: 265px; width: 324px; }
  .slot { position: absolute; left: 0; height: 2px; }
  .slot::before, .slot::after { content: ""; position: absolute; top: 0; height: 1.5px; background: var(--rule); }
  .slot::before { left: 0; width: 173px; }
  .slot::after { left: 179px; width: 145px; }
</style>
</head>
<body>

<section class="card card--front" aria-label="Business card front">
  <div class="stripe"></div>
  <h1 class="doctor-name">Dr. Marisa Tellen</h1>
  <ul class="contact-list">
    <li class="contact-item item-role">
      <svg class="icon" viewBox="0 0 32 24"><circle cx="16" cy="7" r="6" fill="#000"/><path d="M4 24 Q4 13 16 13 Q28 13 28 24 Z" fill="#000"/></svg>
      <span class="label">Chiropractor</span>
    </li>
    <li class="contact-item item-phone">
      <svg class="icon" viewBox="0 0 32 24"><path d="M2 8 Q16 -1 30 8 L28 12 L22 10 L21 7 Q16 5 11 7 L10 10 L4 12 Z" fill="#000"/><path d="M7 13 L11 10 H21 L25 13 V23 H7 Z" fill="#000"/><g fill="#fff"><rect x="11" y="14" width="2" height="2"/><rect x="15" y="14" width="2" height="2"/><rect x="19" y="14" width="2" height="2"/><rect x="11" y="18" width="2" height="2"/><rect x="15" y="18" width="2" height="2"/><rect x="19" y="18" width="2" height="2"/></g></svg>
      <span class="label">519.672.4193</span>
    </li>
    <li class="contact-item item-fax">
      <svg class="icon" viewBox="0 0 32 24"><rect x="8" y="1" width="12" height="11" fill="#000"/><rect x="10" y="3" width="8" height="1.5" fill="#fff"/><rect x="10" y="6" width="8" height="1.5" fill="#fff"/><rect x="3" y="11" width="26" height="12" fill="#000"/><rect x="21" y="7" width="6" height="4" fill="#000"/></svg>
      <span class="label">519.681.2054</span>
    </li>
    <li class="contact-item item-email">
      <svg class="icon" viewBox="0 0 32 24"><rect x="2" y="3" width="28" height="18" fill="none" stroke="#000" stroke-width="2"/><path d="M2 3 L16 14 L30 3 M2 21 L12 11 M30 21 L20 11" fill="none" stroke="#000" stroke-width="2"/></svg>
      <span class="label">marisa.tellen@brevanmail.com</span>
    </li>
    <li class="contact-item item-address">
      <svg class="icon" viewBox="0 0 32 24"><path d="M16 23 Q8 12 8 8 A8 8 0 0 1 24 8 Q24 12 16 23 Z" fill="#000"/><circle cx="16" cy="8" r="3" fill="#fff"/></svg>
      <span class="label">748 Ashcombe Rd North,<br>London, ON N5R 2K9</span>
    </li>
  </ul>
</section>

<section class="card card--back" aria-label="Business card back">
  <div class="stripe"></div>
  <h2 class="appointments-title">Appointments</h2>
  <p class="appointments-note">If you are unable to make your<br>appointment, please call us to reschedule</p>
  <span class="col-head col-date">Date</span>
  <span class="col-head col-time">Time</span>
  <div class="slots">
    <div class="slot" style="top:0"></div>
    <div class="slot" style="top:43px"></div>
    <div class="slot" style="top:88px"></div>
    <div class="slot" style="top:137px"></div>
    <div class="slot" style="top:184px"></div>
    <div class="slot" style="top:230px"></div>
    <div class="slot" style="top:273px"></div>
    <div class="slot" style="top:318px"></div>
    <div class="slot" style="top:367px"></div>
    <div class="slot" style="top:415px"></div>
  </div>
</section>

</body>
</html>
```